Eastlane Holdings Card

I would like a modern, eye catching card based off my logo design.
Info to include:
Tomas Velden (Card Name)
eastlaneholdings.com (Website)
555 283 6091 (Office/fax)
555 736 2840 (Business Cell)
tomas@eastlaneholdings.com (Work email)

Target Market(s)

Commercial real estate brokers, property owners.

Colors
ec1f27
757575

Requirements
Must have
• Name and info above. Not be lame!:)

```html
<!DOCTYPE html>
<html lang="en">
<head>
<meta charset="UTF-8">
<title>Eastlane Holdings – Business Card</title>
<link href="https://fonts.googleapis.com/css2?family=Montserrat:wght@500;700&display=swap" rel="stylesheet">
<style>
  :root {
    --brand-red: #a31d24;
    --brand-grey: #4a4a4a;
    --text-dark: #2b2b2b;
    --card-white: #ffffff;
    --stage: #2b2b2b;
  }
  * { box-sizing: border-box; margin: 0; padding: 0; }
  html, body { width: 1200px; height: 900px; overflow: hidden; }
  body {
    background: var(--stage);
    font-family: "Montserrat", Arial, sans-serif;
    display: flex;
    flex-direction: column;
    align-items: center;
    justify-content: center;
    gap: 48px;
  }
  .card {
    position: relative;
    width: 700px;
    height: 400px;
    background: var(--card-white);
    overflow: hidden;
  }

  /* Front */
  .front .brand {
    position: absolute;
    top: 120px;
    left: 0;
    right: 0;
    display: flex;
    align-items: center;
    justify-content: center;
    gap: 16px;
  }
  .brand-mark {
    width: 34px;
    height: 34px;
    background: var(--brand-red);
  }
  .brand-name {
    color: var(--brand-red);
    font-weight: 700;
    font-size: 38px;
    letter-spacing: 1px;
    text-transform: uppercase;
  }
  .skyline {
    position: absolute;
    left: 0;
    right: 0;
    bottom: 0;
    height: 150px;
    background: var(--brand-red);
  }
  .website {
    position: absolute;
    left: 0;
    right: 0;
    bottom: 56px;
    text-align: center;
    color: var(--card-white);
    font-weight: 700;
    font-size: 15px;
    letter-spacing: 4px;
  }

  /* Back */
  .back .brand {
    position: absolute;
    top: 90px;
    left: 60px;
    display: flex;
    align-items: center;
    gap: 12px;
  }
  .back .brand-mark { width: 26px; height: 26px; }
  .back .brand-name { font-size: 34px; }
  .person {
    position: absolute;
    top: 200px;
    right: 60px;
    text-align: left;
  }
  .person-name {
    color: var(--brand-red);
    font-weight: 700;
    font-size: 15px;
    text-transform: uppercase;
  }
  .person-title {
    color: var(--text-dark);
    font-weight: 500;
    font-size: 13px;
    margin-top: 2px;
  }
  .contact {
    position: absolute;
    left: 0;
    bottom: 46px;
    display: flex;
    align-items: center;
  }
  .icon-tab {
    width: 88px;
    height: 128px;
    background: var(--brand-red);
    border-radius: 0 14px 14px 0;
    display: flex;
    flex-direction: column;
    justify-content: space-around;
    align-items: center;
    padding: 10px 0 10px 24px;
  }
  .icon-tab svg { width: 22px; height: 22px; }
  .contact-list {
    list-style: none;
    margin-left: 18px;
    display: flex;
    flex-direction: column;
    gap: 18px;
    color: var(--text-dark);
    font-size: 15px;
    font-weight: 500;
  }
  .footer-band {
    position: absolute;
    left: 0;
    right: 0;
    bottom: 0;
    height: 60px;
  }
</style>
</head>
<body>

  <section class="card front" aria-label="Card front">
    <div class="brand">
      <span class="brand-mark"></span>
      <span class="brand-name">Eastlane Holdings</span>
    </div>
    <div class="skyline" role="img" aria-label="Red city skyline silhouette along the bottom of the card"></div>
    <p class="website">www.eastlaneholdings.com</p>
  </section>

  <section class="card back" aria-label="Card back">
    <div class="brand">
      <span class="brand-mark"></span>
      <span class="brand-name">Eastlane Holdings</span>
    </div>

    <div class="person">
      <p class="person-name">Tomas Velden</p>
      <p class="person-title">Director / Founder</p>
    </div>

    <div class="contact">
      <div class="icon-tab">
        <svg viewBox="0 0 24 24" fill="none" stroke="#fff" stroke-width="2" aria-hidden="true">
          <rect x="6" y="2" width="12" height="20" rx="2"/><line x1="11" y1="18" x2="13" y2="18"/>
        </svg>
        <svg viewBox="0 0 24 24" fill="#fff" aria-hidden="true">
          <rect x="7" y="3" width="10" height="6"/><rect x="3" y="9" width="18" height="8" rx="1"/><rect x="7" y="14" width="10" height="7" fill="#fff" stroke="#a31d24" stroke-width="1.5"/>
        </svg>
        <svg viewBox="0 0 24 24" fill="none" stroke="#fff" stroke-width="2" aria-hidden="true">
          <rect x="2" y="5" width="20" height="14" rx="1"/><polyline points="2,5 12,13 22,5"/>
        </svg>
      </div>
      <ul class="contact-list">
        <li>555 283 6091</li>
        <li>555 736 2840</li>
        <li>tomas@eastlaneholdings.com</li>
      </ul>
    </div>

    <svg class="footer-band" viewBox="0 0 700 60" preserveAspectRatio="none" aria-hidden="true">
      <rect x="0" y="44" width="700" height="16" fill="var(--brand-grey)"/>
      <path d="M470 60 L470 40 Q470 20 495 20 L700 20 L700 60 Z" fill="var(--brand-red)"/>
      <path d="M458 60 L458 44 L466 44 L466 60 Z" fill="#fff"/>
    </svg>
  </section>

</body>
</html>
```